Anzeigengestaltung für Apotheke
Zielgruppe
Lindmoor-Apotheke
klassische Vor Ort Apotheke, Zielgruppe ältere Menschen und Gesundheitsbewusste Menschen, die ihren Cholesterinwert wissen wollen.
Aufgabenstellung
Keine Speziellen, außer, dass unser Logo in die Anzeige integriert werden soll. Anzeige in DIN A 6 Format und sollte folgenden Inhalt haben:
Irgend ein Teaser : (Gern auch mal im Internet gucken bei anderen Apotheken)
Cholesterin- Woche vom 24.-29. Oktober
Wir messen Ihren Cholesterol Wert inklusive HDL, LDL und Gesamtcholesterin
Anmeldung erbeten bei Frau Hesse: hesse@lindmoor-apotheke.example oder unter 0761 58 72 19

```html
<!DOCTYPE html>
<html lang="de">
<head>
<meta charset="utf-8">
<title>Cholesterin-Woche – Lindmoor-Apotheke</title>
<link href="https://fonts.googleapis.com/css2?family=Open+Sans:ital,wght@0,400;0,700;1,400;1,700&display=swap" rel="stylesheet">
<style>
  :root {
    --green: #1e6a30;
    --green-dark: #175726;
    --mint: #d9efe0;
    --paper: #f6f6f5;
    --backdrop: #e6e7e6;
    --white: #ffffff;
  }
  * { margin: 0; padding: 0; box-sizing: border-box; }
  html, body { width: 1200px; height: 800px; overflow: hidden; }
  body {
    background: var(--backdrop);
    font-family: "Open Sans", Arial, sans-serif;
    color: var(--green);
  }
  .flyer {
    position: absolute;
    left: 50px; top: 10px;
    width: 1100px; height: 780px;
    background: var(--paper);
    overflow: hidden;
    box-shadow: 0 6px 24px rgba(0,0,0,0.18);
  }
  .photo {
    position: absolute;
    left: 520px; top: 0;
    width: 580px; height: 570px;
    background:
      radial-gradient(ellipse at 70% 30%, #f2dcd2 0%, rgba(242,220,210,0) 35%),
      radial-gradient(ellipse at 55% 60%, #ece7ee 0%, rgba(236,231,238,0) 45%),
      linear-gradient(90deg, var(--paper) 0%, #efefef 30%, #f3f1f2 100%);
  }
  .headline {
    position: absolute;
    background: var(--mint);
    font-weight: 700;
    font-style: italic;
    color: var(--green-dark);
    white-space: nowrap;
  }
  .headline--title {
    left: 70px; top: 40px;
    padding: 10px 28px 12px 28px;
    font-size: 60px; line-height: 1.05;
  }
  .headline--date {
    left: 50px; top: 138px;
    padding: 8px 28px 10px 28px;
    font-size: 54px; line-height: 1.05;
  }
  .intro {
    position: absolute;
    left: 40px; top: 238px;
    font-style: italic;
    font-size: 31px; line-height: 1.35;
  }
  .signup {
    position: absolute;
    left: 30px; top: 340px;
    width: 680px; height: 200px;
    border: 3px solid var(--green);
    padding: 16px 24px;
    font-size: 32px; line-height: 1.38;
    font-style: italic;
  }
  .signup strong { font-weight: 700; }
  .footer-band {
    position: absolute;
    left: 0; bottom: 0;
    width: 1100px; height: 210px;
    background: var(--green);
    color: var(--white);
    padding: 30px 40px;
    font-size: 22px; line-height: 1.6;
    white-space: nowrap;
  }
  .footer-band strong { font-weight: 700; }
  .footer-band .sep { padding: 0 10px; }
  .brand-mark {
    position: absolute;
    left: 850px; top: 440px;
    width: 220px; height: 220px;
    border-radius: 50%;
    background: var(--green);
    display: flex; align-items: center; justify-content: center;
    text-align: center;
  }
  .brand-mark span {
    color: var(--white);
    font-weight: 700;
    font-size: 24px;
    line-height: 1.2;
  }
</style>
</head>
<body>
  <main class="flyer">
    <div class="photo" role="img" aria-label="Foto: Apothekerin mit Mundschutz und Handschuhen hält ein Blutröhrchen"></div>

    <h1 class="headline headline--title">Cholesterin- Woche</h1>
    <p class="headline headline--date">vom 24.-29. Oktober</p>

    <p class="intro">Wir messen Ihren Cholesterol Wert<br>inklusive HDL, LDL und Gesamtcholesterin</p>

    <div class="signup">
      Anmeldung erbeten bei Frau Hesse:<br>
      <strong>hesse@lindmoor-apotheke.example</strong><br>
      oder unter <strong>0761 58 72 19</strong>
    </div>

    <footer class="footer-band">
      <strong>Lindmoor-Apotheke</strong><span class="sep">|</span><strong>Apothekerin Dr. Marlene Sauter-Brandt</strong><br>
      Mühlenweg 12 79199 Lindmoor<span class="sep">|</span><strong>T:</strong> (0761) 58 72 19<br>
      <strong>F:</strong> (0761) 58 72 20<span class="sep">|</span>info@lindmoor-apotheke.example<span class="sep">|</span>www.lindmoor-apotheke.example
    </footer>

    <div class="brand-mark"><span>Lindmoor-<br>Apotheke</span></div>
  </main>
</body>
</html>
```